Elegant, High End Integrated Wellness Healthcare Practice

We need a brochure designed for an integrated mind-body wellness healthcare practice (www.larkfernclinic.com) . This brochure will be used when we cold call prospects (physicians to refer to our office, and potential consumers to utilize our services). Our practice is geographically located in the middle Tennessee USA region, although we have plans to become an international company as many of our offerings can be accessed anywhere in the world. Ultimately our goal is to have this brochure used as a leave-behind in an effort to introduce our integrated offerings to increase market share. The final product brochure should be both elegant and serious, with clean lines but also convey warmth and trust, as individuals who are coming for our services have usually struggled with their health for a significant amount of time before finding our practice.
Updates

The design brief was very specific about providing a high-end science-based 2-page brochure (not flier). Several designs submitted were fliers. The other designs were heavy on yoga or "woo woo" non-science-based looking pictures. This is a flier to appeal to physicians and other healthcare providers. Therefore the design must speak science and evidence-based methods of mind and body wellness care. I would also like to appeal to the other designers I paid extra for their submissions and who have indicated they will "respond in the coming days."

```html
<!DOCTYPE html>
<html lang="en">
<head>
<meta charset="utf-8">
<title>Larkfern Wellness Brochure</title>
<link href="https://fonts.googleapis.com/css2?family=Cinzel:wght@500;600;700&family=Poppins:ital,wght@0,300;0,400;0,500;0,600;0,700;1,700&display=swap" rel="stylesheet">
<style>
:root{
  --navy:#172750;
  --green:#72ad42;
  --green-dark:#4f7f2b;
  --leaf:#8cc152;
  --ink:#222222;
  --brand-ink:#24301e;
  --paper:#ffffff;
  --backdrop:#8c8c8c;
  --sky-top:#cfd6e4;
  --sky-mid:#e4e7ee;
  --mountain:#6f93b8;
}
*{margin:0;padding:0;box-sizing:border-box}
html,body{width:893px;height:1200px;overflow:hidden}
body{background:var(--backdrop);font-family:'Poppins',sans-serif;color:var(--ink);position:relative}
.page{position:absolute;width:375px;height:486px;overflow:hidden;background:var(--paper)}
.abs{position:absolute}
.scenery{position:absolute;inset:0}
.sky{background:linear-gradient(180deg,var(--sky-top) 0%,var(--sky-mid) 40%,#b7c7db 62%,var(--mountain) 80%,#4d6d94 100%)}
.bands{position:absolute;inset:0}

/* cover back */
.intro{left:39px;top:33px;width:296px;font-size:8.1px;line-height:11.7px;text-align:justify;hyphens:auto;color:var(--ink)}
.intro p{margin-bottom:8.5px}
.brand-small{left:42px;top:285px;font-family:'Poppins',sans-serif;font-weight:600;font-size:13px;line-height:18px;color:var(--brand-ink)}
.back-title{left:0;width:375px;top:358px;text-align:center;color:#fff;font-family:'Cinzel',serif;font-weight:700;font-size:17px;letter-spacing:.3px}
.back-address{left:0;width:375px;top:388px;text-align:center;color:#fff;font-size:9.5px}
.pill{left:29px;top:407px;width:316px;height:24px;border-radius:12px;background:var(--green);color:#fff;font-weight:600;font-size:8.6px;display:flex;align-items:center;justify-content:center}
.hours{left:0;width:375px;top:436px;text-align:center;color:#fff;font-size:9.4px}
.hours b{font-weight:700}
.web{left:0;width:100%;text-align:center;color:#fff;font-size:10px;letter-spacing:1.6px}

/* cover front */
.brand-large{left:0;width:375px;top:44px;text-align:center;font-family:'Poppins',sans-serif;font-weight:600;font-size:24px;line-height:30px;color:var(--brand-ink)}
.welcome{left:0;width:375px;top:355px;text-align:center;color:var(--green);font-family:'Cinzel',serif;font-weight:700;font-size:18.5px;line-height:21px}
.sub{left:0;width:375px;top:403px;text-align:center;color:#fff;font-family:'Cinzel',serif;font-weight:500;font-size:9.8px;line-height:13px}
.front-rule{left:28px;width:319px;top:441px;height:1px;background:rgba(255,255,255,.25)}
.front-web{top:450px}
.front-web b{color:var(--green);font-weight:700}

/* inside left */
.featured{left:29px;top:31px;font-size:18px;line-height:18px;font-weight:300;color:var(--green);letter-spacing:1.5px}
.label-box{left:29px;width:130px;background:var(--navy);color:var(--green);display:flex;align-items:center;padding-left:10px}
.label-services{top:52px;height:26px;font-weight:700;font-size:17.5px;letter-spacing:1.8px}
.label-other{top:181px;height:25px;font-size:12.5px;font-weight:300}
.label-other b{font-weight:700}
.service-list{left:29px;list-style:none;font-size:10.6px;color:var(--ink)}
.service-list li{height:20.2px;display:flex;align-items:center;gap:5px}
.tick{width:10px;height:10px;flex:none}
.wellness{left:187px;top:34px;width:153px;height:256px;background:var(--green);color:#fff;padding:20px 18px 0 19px}
.wellness h2{font-weight:300;font-size:19px;line-height:22px}
.wellness h2 b{font-weight:700;font-size:20px}
.wellness hr{border:none;border-top:1px solid rgba(255,255,255,.7);margin:17px 0 15px}
.wellness p{font-size:9.8px;line-height:13.4px}
.fold{right:0;bottom:0;width:26px;height:26px}
.practice{left:33px;top:311px;width:307px;font-size:8.4px;line-height:11.6px;text-align:justify;hyphens:auto;color:var(--ink)}
.tagline{font-style:italic;font-weight:700;font-size:8px;color:var(--green)}
.practice-tag{left:33px;top:421px}
.footer{left:0;width:100%;top:444px;height:42px;background:var(--navy);border-top:3px solid var(--green)}
.footer .web{top:13px}

/* inside right */
.portrait{left:0;top:0;width:159px;height:257px;background:radial-gradient(ellipse at 55% 40%,#e9c9a8 0%,#c98f62 35%,#6b4a3c 70%,#3b2c26 100%)}
.approach-panel{left:159px;top:0;width:215px;height:257px;background:linear-gradient(160deg,var(--leaf),var(--green))}
.approach-title{left:181px;top:34px;width:167px;height:25px;background:var(--navy);color:#fff;font-weight:700;font-size:11.4px;display:flex;align-items:center;justify-content:center}
.approach-text{left:181px;top:69px;width:167px;color:#fff;font-size:8.6px;line-height:11.6px;text-align:justify;hyphens:auto}
.approach-tag{left:181px;top:213px;width:167px;color:#fff;font-weight:700;font-size:8.4px;line-height:11px}
.reviews-title{left:33px;top:271px;font-size:13px;color:var(--navy);font-weight:400}
.reviews-title b{font-weight:700}
.reviews-rule{left:33px;top:297px;width:316px;height:1px;background:#555}
.quote{font-size:6.9px;line-height:11px;color:var(--ink);text-align:justify;hyphens:auto}
.quote .by{color:var(--green);font-weight:700;display:block}
.quote-a{left:33px;top:317px;width:90px;text-align:left}
.quote-b{left:154px;top:317px;width:195px}
.qmark{font-family:'Poppins',sans-serif;font-weight:700;font-size:54px;line-height:1;color:#d9d9d9}
</style>
</head>
<body>

<!-- outside spread -->
<section class="page" style="left:72px;top:86px" aria-label="Back cover">
  <div class="scenery sky" role="img" aria-label="Photograph of a cloudy sky over blue mountain ridges"></div>
  <svg class="bands" width="375" height="486" viewBox="0 0 375 486">
    <polygon points="0,315 375,265 375,300 0,363" fill="#72ad42"/>
    <polygon points="0,363 375,300 375,486 0,486" fill="#172750"/>
  </svg>
  <div class="abs intro">
    <p>At Larkfern Wellness we facilitate body and mind health and wellness through an integrated functional approach to care. This method of personalized care appreciates you as a unique individual with distinct health circumstances. We tailor our body and mind approaches to address your specific health concerns. Through the combination of body and mind interventions, we address concerns such as Attention Deficit, Distractibility and learning concerns, chronic pain and inflammation conditions, and mind health conditions such as anxiety, depression, panic, and many more.</p>
    <p>The result is integrative healing-oriented care that addresses aspects of your whole person (body, mind, and spirit). Book a 10 minute consultation to find out how a body and mind consultation can help you live your best life in optimal wellness, call us today or book a consultation online. Please note, this is only for consultation calls regarding our package for a HEALTHY LIFESTYLE FOR LIFE.</p>
    <p>We are conveniently located at 418 Alder Brook Rd. Cedarvale, TN 37190. We serve clients in Cedarvale, Brookmont, Ashgrove, Linden Hollow, Marrow Ridge, Elm Crossing TN, and surrounding areas.</p>
  </div>
  <p class="abs brand-small">Larkfern Wellness</p>
  <h1 class="abs back-title">LARKFERN WELLNESS</h1>
  <p class="abs back-address">418 Alder Brook Rd. Cedarvale, TN 37190</p>
  <p class="abs pill">New Patients: (615) 555 0142&nbsp; / &nbsp;Existing Patients: (615) 555 0187</p>
  <p class="abs hours"><b>OPERATING HOURS :</b> Monday - Friday: 8am - 7pm</p>
  <p class="abs web" style="top:458px">www.larkfernclinic.com</p>
</section>

<section class="page" style="left:447px;top:86px" aria-label="Front cover">
  <div class="scenery sky" role="img" aria-label="Photograph of two hikers raising joined hands on a rocky summit above mountains"></div>
  <svg class="bands" width="375" height="486" viewBox="0 0 375 486">
    <polygon points="0,315 375,265 375,300 0,363" fill="#72ad42"/>
    <polygon points="0,363 375,300 375,486 0,486" fill="#172750"/>
    <polygon points="200,486 375,455 375,486" fill="#72ad42"/>
  </svg>
  <p class="abs brand-large">Larkfern Wellness</p>
  <h2 class="abs welcome">WELCOME TO<br>LARKFERN WELLNESS,</h2>
  <p class="abs sub">INTEGRATED BODY AND MIND HEALTH,<br>WELLNESS CENTER LOCATED IN CEDARVALE, TN</p>
  <div class="abs front-rule"></div>
  <p class="abs web front-web">www.<b>LarkfernClinic</b>.com</p>
</section>

<!-- inside spread -->
<section class="page" style="left:73px;top:633px" aria-label="Inside left page">
  <p class="abs featured">FEATURED</p>
  <p class="abs label-box label-services">SERVICES</p>
  <ul class="abs service-list" style="top:82px">
    <li><svg class="tick" viewBox="0 0 10 10"><circle cx="5" cy="5" r="4.3" fill="none" stroke="#72ad42" stroke-width=".9"/><path d="M3 5.1l1.4 1.4L7 3.8" fill="none" stroke="#72ad42" stroke-width=".9"/></svg>Tonal Brain Care</li>
    <li><svg class="tick" viewBox="0 0 10 10"><circle cx="5" cy="5" r="4.3" fill="none" stroke="#72ad42" stroke-width=".9"/><path d="M3 5.1l1.4 1.4L7 3.8" fill="none" stroke="#72ad42" stroke-width=".9"/></svg>Functional Medicine</li>
    <li><svg class="tick" viewBox="0 0 10 10"><circle cx="5" cy="5" r="4.3" fill="none" stroke="#72ad42" stroke-width=".9"/><path d="M3 5.1l1.4 1.4L7 3.8" fill="none" stroke="#72ad42" stroke-width=".9"/></svg>Healthy Lifestyle For Life</li>
    <li><svg class="tick" viewBox="0 0 10 10"><circle cx="5" cy="5" r="4.3" fill="none" stroke="#72ad42" stroke-width=".9"/><path d="M3 5.1l1.4 1.4L7 3.8" fill="none" stroke="#72ad42" stroke-width=".9"/></svg>Glowpulse For Pain</li>
  </ul>
  <p class="abs label-box label-other">OTHER&nbsp;<b>SERVICES</b></p>
  <ul class="abs service-list" style="top:212px">
    <li><svg class="tick" viewBox="0 0 10 10"><circle cx="5" cy="5" r="4.3" fill="none" stroke="#72ad42" stroke-width=".9"/><path d="M3 5.1l1.4 1.4L7 3.8" fill="none" stroke="#72ad42" stroke-width=".9"/></svg>Whole Body Wellness</li>
    <li><svg class="tick" viewBox="0 0 10 10"><circle cx="5" cy="5" r="4.3" fill="none" stroke="#72ad42" stroke-width=".9"/><path d="M3 5.1l1.4 1.4L7 3.8" fill="none" stroke="#72ad42" stroke-width=".9"/></svg>Brain Wave Mapping</li>
    <li><svg class="tick" viewBox="0 0 10 10"><circle cx="5" cy="5" r="4.3" fill="none" stroke="#72ad42" stroke-width=".9"/><path d="M3 5.1l1.4 1.4L7 3.8" fill="none" stroke="#72ad42" stroke-width=".9"/></svg>Wellness Package</li>
    <li><svg class="tick" viewBox="0 0 10 10"><circle cx="5" cy="5" r="4.3" fill="none" stroke="#72ad42" stroke-width=".9"/><path d="M3 5.1l1.4 1.4L7 3.8" fill="none" stroke="#72ad42" stroke-width=".9"/></svg>Nutritional Wellness</li>
  </ul>
  <div class="abs wellness">
    <h2>WELLNESS<br><b>PACKAGE</b></h2>
    <hr>
    <p>We offer a unique wellness package you won't find anywhere else, a combination of a body and mind system designed to "Reunite" your brain and your gut!</p>
    <svg class="abs fold" viewBox="0 0 26 26"><polygon points="26,0 0,26 26,26" fill="#fff"/><polygon points="26,0 0,26 0,0" fill="#4f7f2b"/></svg>
  </div>
  <p class="abs practice">The practitioners at Larkfern Wellness have significant experience working with whole-body approaches to care. Whole body health requires that the body and mind are aligned. Although pharmaceuticals and "talk therapy" can be beneficial we have found that these methods often fall short to address concerns that brought the individual to our office. Body changes are often missing. When one's body changes the mind can more readily integrate other parts of a person's approach to life. The result is integrative healing-oriented care that addresses aspects of the whole person (body, mind, and spirit).</p>
  <p class="abs tagline practice-tag">Find a clearer path to lasting health</p>
  <div class="abs footer"><p class="abs web">www.larkfernclinic.com</p></div>
</section>

<section class="page" style="left:446px;top:633px" aria-label="Inside right page">
  <div class="abs portrait" role="img" aria-label="Photograph of a woman in a knit hat with eyes closed in warm sunlight"></div>
  <div class="abs approach-panel"></div>
  <h3 class="abs approach-title">OUR UNIQUE APPROACH</h3>
  <p class="abs approach-text">At Larkfern Wellness we facilitate body and mind health and wellness through an integrated functional approach to care. This method of personalized care appreciates you as a unique individual with distinct health circumstances. We tailor our body and mind approaches to address your specific health concerns. The result is integrative healing-oriented care that addresses aspects of your whole person (body, mind, and spirit).</p>
  <p class="abs approach-tag">Find a clearer path to lasting health</p>
  <h3 class="abs reviews-title">PATIENT REVIEWS <b>AND FEEDBACK</b></h3>
  <div class="abs reviews-rule"></div>
  <span class="abs qmark" style="left:30px;top:297px">“</span>
  <span class="abs qmark" style="left:92px;top:400px">”</span>
  <span class="abs qmark" style="left:150px;top:297px">“</span>
  <span class="abs qmark" style="left:318px;top:400px">”</span>
  <p class="abs quote quote-a">Dr. Hale is amazing at giving advice on how to handle different situations. Amazing listener and very good at explaining how to figure out certain behaviors or feelings one may be experiencing.<span class="by">JK</span></p>
  <p class="abs quote quote-b">I have been seeing Dr. Hale for some time now and cannot say enough about how grateful I am to have found her! She is professional and easy to talk to. She has established a warm and welcoming environment where you feel comfortable speaking freely. Dr. Hale is straightforward, which I LOVE! The receptionist is the sweetest! They are very accommodating and offer zoom sessions as well as in person. My daughter sees Dr Moreno which we have been happy with as well. I highly recommend this team!<span class="by">Mira T.</span></p>
  <div class="abs footer"><p class="abs web">www.larkfernclinic.com</p></div>
</section>

</body>
</html>
```